Systems and Technology Consultants - Website

Design & Build a website for a new company which operates in the Systems and Technology space for Transportation, Government and Commercial sectors.

Overall design should be minimalist in nature.
Should also have a feed that provides news and event updates on the main page.
Logo has already been awarded and should be incorporated into the site.

We like the overall layout, functionality and simplicity of the below sites. Submitted designs could be similar to or a combination of the aspects on these sites, or perhaps a whole different concept - we are open to new ideas.
Vortrane.com
Merp.it

Update 1 Dated 27 May 2014

All I am moving away from the Merp.it website and would like it to be more aligned with Vortrane.com not only in layout but in functionality. I will be extending the deadline of this design brief for two weeks to incorporate additional requirements and will add addtional funding to the project.

Apologies for not having more information available to provide but with so many submissions its getting confusing.

Thanks Dermot
Updates

Please note that the brief has been updated and the deadline has been extended.

Important: We will need two language versions of the website, English and Arabic; the website is hosted on HostPeak

Hello All, Thank you for your submissions. We have narrowed it down to the final 6 designers and I just wanted to take a moment and provide a bit of feedback regarding the concepts that we like and the modifications we are looking for. First, let me mention some of the design functions we like. - At the top of the homepage we really like the "region" or "language" tab so that the website can be viewed in both English and Arabic. - We like the homepage to have clear color variation so that the different sections of the homepage are distinct. Additionally, we like the bottom portion of the homepage to be in red. We feel that draws attention to our contact information. Again, we would like the colors to integrate black, gray-scale, red, etc. - Having a search tab at the top of the home page, or integrated into the main image, so that the site is easy to navigate. - We especially like the main image to have the scrolling tabs at the bottom so it is easy to browse the services offered (Consultancy, Solutions Architecture, Masters Systems Integration, Independent Design Review). - In regards to the services offered tab we really like the idea that a few people presented that have the outside of our logo with an icon in the middle of consultancy, solutions, etc., etc. Secondly, as mentioned in our brief we really enjoy the design of vortrane site. Specially, we enjoy the strong iconic images they use, the way the tabs at the top scroll easily, and contact us page that generates an email. Lastly, I've included some photos of the concept we have been working on. What we are trying to demonstrate is how our company offers a range of services that are essentially linked together. We provide individual services that when combined present the full service package. We would like this concept to be integrated into the over concept of our website. Please feel free to ask for clarification of any of the above points or contact us if you have any additional questions. We appreciate all of your hard work and are very excited to see the updated designs. Best, Miriam Dowbrook Plenvaro Senior Program Manager miriam.dowbrook@plenvaro-mail.com

Industry/Entity Type

Government

Font styles to use
Serif
Sans Serif

Requirements
Must have
• Must work on/adapt to various/mobile devices (responsive)
Must be simple and straightforward
Colors should be in line/matching with logo
2 language versions: English and Arabic (no Thai)
Services should be the first group/row of items after/below the main image
Note: the website will be hosted by hostpeak
Nice to have
• Submit feedback form
What's New section
The banner at the bottom of the site should not be too large; we would like a narrow one more
It would be nice if the header/top banner (with Home, About, etc. tabs) could stay in place as you scroll down (like Vortrane and Chatterly)
We will likely only use one image with a Company slogan on the Home page rather than a carousel of images to rotate through
Should not have
• This is the existing website: http://www.plenvaro-example.org
We do not like the animation, the way the banner icons/titles bounce
Not simple enough, we don't like the functionality or how pages load so slowly
We do not like the logo centered - it should be at the left
The banner and its tabs should not be towards the right, we would like them to be centered, to go all the way across and to be below the logo

```html
<!DOCTYPE html>
<html lang="en">
<head>
<meta charset="utf-8">
<title>Plenvaro – Home</title>
<link rel="stylesheet" href="https://fonts.googleapis.com/css2?family=Open+Sans:ital,wght@0,300;0,400;0,600;0,700;1,400&display=swap">
<style>
:root{
  --red:#e3161f;
  --ink:#222;
  --text:#555;
  --muted:#8a8a8a;
  --line:#e6e6e6;
  --tab-bg:#f3f3f3;
  --tab-active:#e9e9e9;
  --footer:#3a3a3a;
  --footer-base:#2f2f2f;
  --footer-text:#b3b3b3;
  --footer-line:#4d4d4d;
}
*{margin:0;padding:0;box-sizing:border-box}
html,body{width:1200px;height:1195px;overflow:hidden;background:#fff}
body{position:relative;font-family:"Open Sans",Arial,sans-serif;color:var(--ink)}
.top-rule{position:absolute;left:0;top:0;width:1200px;height:4px;background:var(--red)}

.brand{position:absolute;left:138px;top:44px;display:flex;align-items:center;gap:10px}
.brand-mark{width:22px;height:22px;background:var(--red)}
.brand-name{font-weight:700;font-size:22px;color:var(--red);letter-spacing:2px}

.main-nav{position:absolute;left:270px;top:0;width:810px;height:90px;border-bottom:1px solid var(--line)}
.nav-item{position:absolute;top:38px;text-align:left}
.nav-item .label{display:block;font-weight:700;font-size:13px;color:var(--ink);letter-spacing:.2px}
.nav-item .hint{display:block;font-style:italic;font-size:11px;color:#aaa;margin-top:2px}
.nav-item.is-active{top:0;left:190px;width:105px;height:90px;background:#f7f7f7;border-top:4px solid #9a9a9a;padding-top:34px;text-align:center}
.nav-item.is-active .label{color:var(--red)}
.nav-item.is-active::after{content:"";position:absolute;left:49px;bottom:-5px;border:5px solid transparent;border-bottom:0;border-top-color:var(--red)}

.tagline{position:absolute;left:0;top:157px;width:1200px;text-align:center;font-weight:300;font-size:20px;line-height:24px;color:#3c3c3c}

.hero{position:absolute;left:120px;top:234px;width:959px;height:376px;border-radius:6px 6px 0 0;overflow:hidden;
  background:linear-gradient(100deg,#f4f6f8 0%,#e8edf1 35%,#c9d3db 60%,#8e98a2 82%,#7a838c 100%)}
.hero-photo{position:absolute;right:0;top:0;width:480px;height:376px;
  background:radial-gradient(ellipse at 60% 60%,rgba(40,46,66,.55),rgba(120,130,140,0) 70%)}
.hero-title{position:absolute;left:50px;top:106px;font-size:50px;line-height:60px;font-weight:400;color:var(--red);letter-spacing:-1px}

.service-strip{position:absolute;left:120px;top:610px;width:959px;height:87px}
.service-strip::before{content:"";position:absolute;left:0;top:0;width:710px;height:5px;background:#9c9c9c}
.service-strip::after{content:"";position:absolute;left:710px;top:0;width:249px;height:5px;background:var(--red)}
.service-tab{position:absolute;top:5px;height:82px;background:var(--tab-bg);display:flex;align-items:center;padding-left:16px;gap:9px}
.service-tab + .service-tab{border-left:2px solid #fff}
.service-tab.is-active{background:var(--tab-active);box-shadow:0 14px 14px -10px rgba(0,0,0,.35)}
.service-icon{width:38px;height:38px;flex:none}
.service-name{font-size:16px;font-weight:600;color:#333;line-height:18px}
.service-tab.is-active .service-name{color:var(--red)}
.service-note{font-size:12px;font-weight:300;color:#777}

.section-title{position:absolute;top:754px;font-size:20px;font-weight:400;color:var(--red)}
.article{position:absolute;left:119px;width:460px}
.article-thumb{position:absolute;left:0;top:0;width:64px;height:68px;border:1px solid #ddd;
  background:linear-gradient(160deg,#e4eef2,#9fb3bd 55%,#dbe6ea)}
.article-body{position:absolute;left:73px;top:-4px;width:385px}
.item-title{font-size:15px;color:var(--ink);line-height:20px}
.item-text{font-size:13px;color:var(--muted);line-height:15px;margin-top:4px}
.read-more{display:inline-block;margin-top:7px;font-size:12px;color:#444;text-decoration:underline}

.news{position:absolute;left:696px;width:400px}
.date-badge{position:absolute;left:0;top:0;width:62px;height:58px;text-align:center;color:#fff;border-radius:2px;overflow:hidden;box-shadow:0 1px 2px rgba(0,0,0,.3)}
.date-day{height:30px;background:#444;font-size:24px;line-height:32px}
.date-month{height:28px;background:var(--red);font-size:20px;line-height:26px}
.news-body{position:absolute;left:73px;top:-4px;width:330px}

.site-footer{position:absolute;left:0;top:1021px;width:1200px;height:133px;background:var(--footer)}
.site-footer::before{content:"";position:absolute;left:589px;top:0;border:9px solid transparent;border-bottom:0;border-top-color:#fff}
.footer-links{position:absolute;left:131px;top:40px;font-size:11px;color:var(--footer-text)}
.footer-links span{margin-right:8px}
.footer-links .sep{color:#888}
.footer-rule{position:absolute;top:64px;height:1px;background:var(--footer-line)}
.contact-row{position:absolute;left:131px;top:78px;font-size:11px;color:var(--footer-text);display:flex;align-items:center}
.contact-row .item{display:flex;align-items:center;gap:9px}
.social-title{position:absolute;left:848px;top:37px;font-size:11px;color:var(--footer-text);letter-spacing:.3px}
.social-row{position:absolute;left:848px;top:76px;display:flex;gap:18px}
.social-dot{width:17px;height:17px;border-radius:3px;background:#8a8a8a}

.base-bar{position:absolute;left:0;top:1154px;width:1200px;height:41px;background:var(--footer-base);font-size:11px;color:var(--footer-text)}
.base-bar span{position:absolute;top:14px}
.base-bar .divider{top:12px;width:1px;height:18px;background:#4f4f4f}
</style>
</head>
<body>
<div class="top-rule"></div>

<header>
  <div class="brand"><span class="brand-mark"></span><span class="brand-name">PLENVARO</span></div>
  <nav class="main-nav">
    <a class="nav-item is-active"><span class="label">HOME</span><span class="hint">all strats here</span></a>
    <a class="nav-item" style="left:315px"><span class="label">BUSINESS UNITS</span><span class="hint">work we are proud of</span></a>
    <a class="nav-item" style="left:440px"><span class="label">SERVICES</span><span class="hint">what we think</span></a>
    <a class="nav-item" style="left:530px"><span class="label">ABOUT US</span><span class="hint">know about us</span></a>
    <a class="nav-item" style="left:625px"><span class="label">LOCATIONS</span><span class="hint">about places</span></a>
    <a class="nav-item" style="left:727px"><span class="label">CONTACT US</span><span class="hint">enquire here</span></a>
  </nav>
</header>

<p class="tagline">Plenvaro specializes in delivering quality professional services and technical projects<br>that support larger business goals.</p>

<section class="hero">
  <div class="hero-photo" role="img" aria-label="Businessman in a suit using a tablet against a cloudy sky with a faint world map"></div>
  <h1 class="hero-title">Plenvaro<br>International</h1>
</section>

<div class="service-strip">
  <div class="service-tab" style="left:0;width:238px">
    <svg class="service-icon" viewBox="0 0 38 38"><circle cx="19" cy="19" r="19" fill="#333"/><circle cx="19" cy="19" r="8" fill="none" stroke="#fff" stroke-width="3" stroke-dasharray="3 2.3"/><circle cx="19" cy="19" r="3" fill="#fff"/></svg>
    <div><div class="service-name">Consulting</div><div class="service-note">Lorem Ipsum is simply</div></div>
  </div>
  <div class="service-tab" style="left:238px;width:236px;padding-left:18px">
    <svg class="service-icon" viewBox="0 0 38 38"><circle cx="19" cy="19" r="19" fill="#333"/><circle cx="19" cy="14" r="5" fill="#fff"/><path d="M10 30c1-6 5-9 9-9s8 3 9 9z" fill="#fff"/></svg>
    <div><div class="service-name">Engineering</div><div class="service-note">Lorem Ipsum is simply</div></div>
  </div>
  <div class="service-tab" style="left:474px;width:236px">
    <svg class="service-icon" viewBox="0 0 38 38"><circle cx="19" cy="19" r="19" fill="#333"/><rect x="9" y="20" width="16" height="6" fill="#fff"/><path d="M14 20l5-9 9 4-2 2-6-2-3 5z" fill="#fff"/><circle cx="12" cy="28" r="2" fill="#fff"/><circle cx="22" cy="28" r="2" fill="#fff"/></svg>
    <div><div class="service-name">Construction</div><div class="service-note">Lorem Ipsum is simply</div></div>
  </div>
  <div class="service-tab is-active" style="left:710px;width:249px">
    <svg class="service-icon" viewBox="0 0 38 38"><circle cx="19" cy="19" r="19" fill="#333"/><circle cx="20" cy="19" r="10" fill="none" stroke="#fff" stroke-width="2"/><path d="M10 19h20M20 9v20M13 13h14M13 25h14" stroke="#fff" stroke-width="1.5"/></svg>
    <div><div class="service-name">Operations</div><div class="service-note">Lorem Ipsum is simply</div></div>
  </div>
</div>

<h2 class="section-title" style="left:121px">Our Articles</h2>
<article class="article" style="top:790px">
  <div class="article-thumb" role="img" aria-label="Close-up of a spiral notebook binding"></div>
  <div class="article-body">
    <h3 class="item-title">It is a long established fact that</h3>
    <p class="item-text">It is a long established fact that a reader will be distracted by the readable content of a page when looking at its layout.</p>
    <a class="read-more">Read More</a>
  </div>
</article>
<article class="article" style="top:894px">
  <div class="article-thumb" role="img" aria-label="Close-up of a spiral notebook binding"></div>
  <div class="article-body">
    <h3 class="item-title">It is a long established fact that</h3>
    <p class="item-text">It is a long established fact that a reader will be distracted by the readable content of a page when looking at its layout.</p>
    <a class="read-more">Read More</a>
  </div>
</article>

<h2 class="section-title" style="left:696px">Our News</h2>
<article class="news" style="top:797px">
  <div class="date-badge"><div class="date-day">27</div><div class="date-month">Feb</div></div>
  <div class="news-body">
    <h3 class="item-title">Lorem ipsum dolor sit amet,</h3>
    <p class="item-text">Lorem Ipsum is simply dummy text of the printing and typesetting industry</p>
  </div>
</article>
<article class="news" style="top:899px">
  <div class="date-badge"><div class="date-day">23</div><div class="date-month">Feb</div></div>
  <div class="news-body">
    <h3 class="item-title">Lorem ipsum dolor sit amet,</h3>
    <p class="item-text">Lorem Ipsum is simply dummy text of the printing and typesetting industry.</p>
  </div>
</article>

<footer class="site-footer">
  <div class="footer-links">
    <span>Home</span><span class="sep">|</span>
    <span>About Us</span><span class="sep">|</span>
    <span>Business Unit</span><span class="sep">|</span>
    <span>Services</span><span class="sep">|</span>
    <span>Locations</span><span class="sep">|</span>
    <span>Contact Us</span>
  </div>
  <div class="footer-rule" style="left:128px;width:700px"></div>
  <div class="contact-row">
    <span class="item">
      <svg width="16" height="14" viewBox="0 0 16 14"><path d="M8 0l8 7h-2v7H10V9H6v5H2V7H0z" fill="#8a8a8a"/></svg>
      Lorem Ipsum is simply dummy text of the printinge
    </span>
    <span class="item" style="margin-left:55px">
      <svg width="16" height="16" viewBox="0 0 16 16"><path d="M3 1l3 3-2 2c1 2 3 4 6 6l2-2 3 3-2 2C7 15 1 9 1 3z" fill="#8a8a8a"/></svg>
      (123) 456-7890
    </span>
    <span class="item" style="margin-left:24px">
      <svg width="15" height="11" viewBox="0 0 15 11"><rect width="15" height="11" fill="#8a8a8a"/><path d="M0 0l7.5 6L15 0" fill="none" stroke="#3a3a3a" stroke-width="1.3"/></svg>
      contact@companyname.com
    </span>
  </div>
  <div class="social-title">STAY CONNECTED</div>
  <div class="footer-rule" style="left:848px;width:221px"></div>
  <div class="social-row">
    <span class="social-dot" style="border-radius:50%"></span>
    <span class="social-dot"></span>
    <span class="social-dot" style="border-radius:50%"></span>
    <span class="social-dot"></span>
    <span class="social-dot"></span>
    <span class="social-dot"></span>
  </div>
</footer>

<div class="base-bar">
  <span style="left:126px">Plenvaro © 2014</span>
  <span class="divider" style="left:230px"></span>
  <span style="left:246px">Legal Notice</span>
  <span class="divider" style="left:328px"></span>
  <span style="left:345px">Terms</span>
</div>
</body>
</html>
```